TovaLamarpe - Israeli Mental Health Website

We are developing an Israeli website for mental health. The website will be both in English and in Hebrew. We have a logo and would like a website design based on the logo and the logos colors (attached).

Attached is a doc that contains the website requirements.

We would like to have an icon for each of the sidebar categories, an image for each of the pages (including each of the sidebar category pages).

Target Market(s)

Adults 18-80

Industry/Entity Type

Mental Health

Number of Pages Required

5+ page

Font styles to use
Sans Serif

Colors

Designer to choose colors to be used in the design.

```html
<!DOCTYPE html>
<html lang="en">
<head>
<meta charset="utf-8">
<title>TovaLamarpe — Therapists search page</title>
<link href="https://fonts.googleapis.com/css2?family=Inter:wght@400;500;600;700;800&family=Poppins:wght@300;400;500&display=swap" rel="stylesheet">
<style>
:root{
  --main:#1e76c2;
  --green:#4dae45;
  --extra:#f0f3f8;
  --dark:#262a3c;
  --grey:#8e90a6;
  --light-grey:#e2e3eb;
  --light-grey-2:#f1f1f3;
  --text:#2b2f3a;
  --muted:#9aa0ae;
  --blob:#e6eef7;
  --white:#fff;
}
*{margin:0;padding:0;box-sizing:border-box}
html,body{width:1200px;height:2451px;overflow:hidden}
body{position:relative;background:var(--white);font-family:"Inter",sans-serif;color:var(--text)}
.abs{position:absolute}
.blob{position:absolute;border-radius:50%;background:var(--blob)}

.brand-mark{left:57px;top:60px;display:flex;align-items:center;gap:8px;font:600 16px "Inter",sans-serif;color:var(--main)}
.brand-mark .dot{width:12px;height:12px;border-radius:50%;background:var(--main)}
.made-with{left:980px;top:60px;font:400 18px "Poppins",sans-serif;color:#c4c8d0;white-space:nowrap}

.tags{left:0;width:1200px;top:150px;text-align:center;font:400 17px "Poppins",sans-serif;color:#c3c6cd;word-spacing:8px}
.headline{left:0;width:1200px;top:190px;text-align:center;font:500 34px/41px "Inter",sans-serif;color:#111}
.headline strong{font-weight:800}
.headline .stop{color:var(--main);font-weight:800}
.caption{left:0;width:1200px;top:342px;text-align:center;font:400 15px "Inter",sans-serif;color:#222}

.page{left:60px;top:402px;width:1080px;height:1570px;background:var(--extra);border-radius:12px;box-shadow:0 6px 30px rgba(40,60,100,.08);overflow:hidden}
.nav{left:0;top:0;width:1080px;height:59px;background:var(--white)}
.nav .logo{left:111px;top:20px;display:flex;align-items:center;gap:6px;font:600 12px "Inter",sans-serif;color:var(--main)}
.nav .logo .dot{width:9px;height:9px;border-radius:50%;background:var(--green)}
.nav-links{left:431px;top:24px;display:flex;gap:17px;font:500 10px "Inter",sans-serif;color:#333;white-space:nowrap}
.nav-divider{left:872px;top:19px;width:1px;height:20px;background:var(--green)}
.lang{left:897px;top:24px;font:500 10px "Inter",sans-serif;color:#999;display:flex;gap:9px}
.lang .on{color:var(--main);font-weight:600}

.hero{left:0;top:59px;width:1080px;height:162px;background:linear-gradient(90deg,#2a5fa0 0%,#3b78bd 45%,#6d9dd0 70%,#4a80c0 100%)}
.hero-title{left:111px;top:108px;font:700 26px "Inter",sans-serif;color:var(--white)}
.hero-copy{left:111px;top:146px;font:400 11px/16px "Inter",sans-serif;color:#e8f0fa}

.crumbs{left:111px;top:232px;font:400 10px "Inter",sans-serif;color:#777;display:flex;gap:6px;align-items:center}
.crumbs .here{color:var(--main);font-weight:600}
.share{left:924px;top:232px;font:500 10px "Inter",sans-serif;color:#333;display:flex;gap:8px;align-items:center}
.rule{left:111px;top:255px;width:857px;height:1px;background:#e1e5ec}

.tab{left:184px;top:290px;width:123px;height:26px;background:var(--green);border-radius:10px 24px 0 0;font:600 9.5px "Inter",sans-serif;color:var(--white);padding:9px 0 0 12px}
.filters{left:184px;top:315px;width:712px;height:256px;background:var(--white);border-radius:0 14px 14px 14px;box-shadow:0 4px 14px rgba(40,60,100,.05)}
.label{position:absolute;font:600 9px "Inter",sans-serif;color:#222}
.select{position:absolute;width:137px;height:26px;border:1px solid #dde1e8;border-radius:5px;font:400 9px "Inter",sans-serif;color:#9aa0ae;padding:7px 0 0 11px}
.select svg{position:absolute;right:12px;top:9px}
.checks{position:absolute;font:400 9px "Inter",sans-serif;color:#444}
.checks div{height:19px;display:flex;align-items:center;gap:6px}
.box{width:9px;height:9px;border:1px solid #777;border-radius:1px;display:inline-flex;align-items:center;justify-content:center}
.box.on{border-color:var(--green)}
.btn{position:absolute;background:var(--main);color:var(--white);border-radius:16px;font:600 10.5px "Inter",sans-serif;display:flex;align-items:center;justify-content:center}
.chip{position:absolute;height:27px;border:1px solid #dde1e8;border-radius:5px;font:400 9px "Inter",sans-serif;color:#9aa0ae;padding:0 10px;display:flex;align-items:center;justify-content:space-between}
.chip .box{border-color:#666}
.chip.active{border-color:var(--green);color:var(--green)}
.chip.active .box{border-color:var(--green)}

.result{left:184px;width:712px;height:102px;background:var(--white);border-radius:12px;box-shadow:0 4px 14px rgba(40,60,100,.04)}
.avatar{position:absolute;left:28px;top:21px;width:59px;height:59px;border-radius:50%}
.badge{position:absolute;left:70px;top:64px}
.r-name{position:absolute;left:106px;top:24px;font:600 12.5px "Inter",sans-serif;color:#1d2230}
.r-sub{position:absolute;left:106px;top:46px;font:400 9.5px/18px "Inter",sans-serif;color:#6f7585}
.r-div{position:absolute;left:227px;top:24px;width:1px;height:54px;background:#e6e8ee}
.r-meta{position:absolute;left:247px;top:24px;font:400 9.5px/20.5px "Inter",sans-serif;color:#9aa0ae}
.r-meta b{font-weight:600;color:#222;margin-right:6px}
.r-btn{left:595px;top:20px;width:90px;height:30px}
.r-pay{position:absolute;left:595px;width:90px;top:59px;text-align:center;font:400 9.5px/12px "Inter",sans-serif;color:#6f7585}

.suggest{left:0;width:1080px;top:1225px;text-align:center;font:400 9.5px "Inter",sans-serif;color:#333}
.suggest a{color:var(--main);font-weight:600;text-decoration:underline}
.rule-2{left:130px;top:1279px;width:821px;height:1px;background:#dfe3ea}

.feature{position:absolute;top:1339px;width:196px}
.feature h3{font:600 14px "Inter",sans-serif;color:#1d2b4a;margin-top:4px}
.feature p{font:400 10.5px/18px "Inter",sans-serif;color:#7c8292;margin-top:8px}
.feature .more{margin-top:12px;font:600 10.5px "Inter",sans-serif;color:var(--green);display:flex;gap:10px;align-items:center}
.f-icon{position:absolute;top:1344px}
.col-rule{position:absolute;top:1339px;width:1px;height:124px;background:#e1e5ec}
.foot-rule{left:111px;top:1514px;width:857px;height:1px;background:#e1e5ec}
.foot{top:1535px;font:400 9px "Inter",sans-serif;color:#9aa0ae;white-space:nowrap}
.foot-links{display:flex;gap:10px}

.sec-title{left:63px;font:400 12px "Poppins",sans-serif;letter-spacing:3px;color:#7a7e88}
.sec-copy{left:63px;font:400 10px "Poppins",sans-serif;color:#222}
.swatch{position:absolute;width:127px;height:72px}
.sw-name{position:absolute;font:400 15px "Poppins",sans-serif;color:#555}
.sw-hex{position:absolute;font:400 11px "Poppins",sans-serif;color:#aaa}
</style>
</head>
<body>

<div class="blob" style="left:-120px;top:-120px;width:240px;height:220px"></div>
<div class="blob" style="left:1080px;top:-110px;width:260px;height:200px"></div>
<div class="blob" style="left:950px;top:320px;width:420px;height:420px"></div>
<div class="blob" style="left:-200px;top:380px;width:300px;height:380px"></div>
<div class="blob" style="left:-180px;top:1050px;width:320px;height:420px"></div>
<div class="blob" style="left:1080px;top:960px;width:240px;height:180px"></div>
<div class="blob" style="left:1080px;top:1440px;width:260px;height:260px"></div>
<div class="blob" style="left:950px;top:1860px;width:420px;height:160px"></div>

<div class="abs brand-mark"><span class="dot"></span>TovaLamarpe</div>
<div class="abs made-with">Made with Planora</div>

<div class="abs tags">#WEB DESIGN &nbsp;#UI/UX DESIGN &nbsp;#2023</div>
<div class="abs headline"><strong>TovaLamarpe</strong><span class="stop">.</span> Israeli website<br>for mental health</div>
<div class="abs caption">Therapists search page</div>

<main class="abs page">
  <header class="abs nav">
    <div class="abs logo"><span class="dot"></span>TovaLamarpe</div>
    <nav class="abs nav-links">
      <span>Smart Chatline</span><span>Therapists</span><span>Organizations</span><span>Videos</span><span>Contact</span><span>About</span><span>Donate</span>
    </nav>
    <div class="abs nav-divider"></div>
    <div class="abs lang"><span class="on">English</span><span>עברית</span></div>
  </header>

  <div class="abs hero" role="img" aria-label="Photo of therapists talking with patients in a bright office, tinted blue"></div>
  <h1 class="abs hero-title">Therapists</h1>
  <p class="abs hero-copy">Lorem ipsum dolor sit amet, consectetur adipiscing elit,<br>sed do eiusmod tempor incididunt ut labore et dolore magna aliqua.</p>

  <div class="abs crumbs"><span>Home</span>
    <svg width="7" height="8" viewBox="0 0 7 8"><path d="M2 1l3 3-3 3" fill="none" stroke="#1e76c2" stroke-width="1.3"/></svg>
    <span class="here">Therapists</span></div>
  <div class="abs share">
    <svg width="10" height="10" viewBox="0 0 10 10"><circle cx="2" cy="5" r="1.3" fill="none" stroke="#bbb"/><circle cx="8" cy="2" r="1.3" fill="none" stroke="#bbb"/><circle cx="8" cy="8" r="1.3" fill="none" stroke="#bbb"/><path d="M3 4.5l4-2M3 5.5l4 2" stroke="#bbb"/></svg>
    Share</div>
  <div class="abs rule"></div>

  <div class="abs tab">Find your therapist</div>
  <section class="abs filters">
    <div class="label" style="left:28px;top:25px">Area</div>
    <div class="select" style="left:28px;top:41px">Choose your area
      <svg width="8" height="6" viewBox="0 0 8 6"><path d="M1 1l3 3 3-3" fill="none" stroke="#666" stroke-width="1.2"/></svg></div>
    <div class="label" style="left:193px;top:25px">Sub-Category</div>
    <div class="select" style="left:193px;top:41px">Sub-Category
      <svg width="8" height="6" viewBox="0 0 8 6"><path d="M1 1l3 3 3-3" fill="none" stroke="#666" stroke-width="1.2"/></svg></div>
    <div class="abs" style="left:28px;top:85px;width:302px;height:1px;background:#e6e8ee"></div>

    <div class="label" style="left:28px;top:106px">Payment</div>
    <div class="checks" style="left:28px;top:119px">
      <div><span class="box on"><svg width="7" height="6" viewBox="0 0 7 6"><path d="M1 3l2 2 3-4" fill="none" stroke="#4dae45" stroke-width="1.2"/></svg></span>Free</div>
      <div><span class="box"></span>Subsidized</div>
      <div><span class="box on"><svg width="7" height="6" viewBox="0 0 7 6"><path d="M1 3l2 2 3-4" fill="none" stroke="#4dae45" stroke-width="1.2"/></svg></span>Full Cost</div>
    </div>
    <div class="label" style="left:194px;top:106px">Therapist Gender</div>
    <div class="checks" style="left:194px;top:119px">
      <div><span class="box on"><svg width="7" height="6" viewBox="0 0 7 6"><path d="M1 3l2 2 3-4" fill="none" stroke="#4dae45" stroke-width="1.2"/></svg></span>Any</div>
      <div><span class="box"></span>Man</div>
      <div><span class="box"></span>Woman</div>
    </div>
    <div class="btn" style="left:28px;top:205px;width:80px;height:31px">Search</div>

    <div class="abs" style="left:350px;top:24px;width:1px;height:216px;background:#e6e8ee"></div>
    <div class="label" style="left:370px;top:25px">Category</div>
    <div class="chip active" style="left:370px;top:42px;width:317px;height:26px">General
      <span class="box"><svg width="7" height="6" viewBox="0 0 7 6"><path d="M1 3l2 2 3-4" fill="none" stroke="#4dae45" stroke-width="1.2"/></svg></span></div>
    <div class="chip" style="left:370px;top:76px;width:153px">Emergency Mental Help<span class="box"></span></div>
    <div class="chip" style="left:533px;top:76px;width:154px">Suicide<span class="box"></span></div>
    <div class="chip" style="left:370px;top:110px;width:153px">Sexual Assault/Violence<span class="box"></span></div>
    <div class="chip" style="left:533px;top:110px;width:154px">Post Trauma<span class="box"></span></div>
    <div class="chip" style="left:370px;top:144px;width:153px">Depression<span class="box"></span></div>
    <div class="chip" style="left:533px;top:144px;width:154px">Anxiety<span class="box"></span></div>
    <div class="chip" style="left:370px;top:177px;width:153px">Addictions<span class="box"></span></div>
    <div class="chip" style="left:533px;top:177px;width:154px">Sleep Disorders<span class="box"></span></div>
    <div class="chip" style="left:370px;top:211px;width:153px">Addictions<span class="box"></span></div>
    <div class="chip" style="left:533px;top:211px;width:154px">Sleep Disorders<span class="box"></span></div>
    <div class="abs" style="left:695px;top:42px;width:2px;height:198px;background:#e6e8ee"></div>
    <div class="abs" style="left:695px;top:42px;width:2px;height:133px;background:var(--main)"></div>
  </section>

  <article class="abs result" style="top:607px">
    <div class="avatar" role="img" aria-label="Portrait photo of the therapist" style="background:linear-gradient(#d9dde3,#eef0f3)"></div>
    <svg class="badge" width="14" height="14" viewBox="0 0 14 14"><circle cx="7" cy="7" r="7" fill="#4dae45"/><path d="M4 7l2 2 4-4" fill="none" stroke="#fff" stroke-width="1.5"/></svg>
    <div class="r-name">Dr. Noam Levin</div>
    <div class="r-sub">General Therapist<br>MBBS / FCPS</div>
    <div class="r-div"></div>
    <div class="r-meta"><b>Area:</b>City 1<br><b>Category:</b>General, Emergency Mental Help<br><b>Sub-category:</b>Sub-category1</div>
    <div class="btn r-btn">Call Now</div>
    <div class="r-pay">Payment: Free<br>from: $300</div>
  </article>
  <article class="abs result" style="top:726px">
    <div class="avatar" role="img" aria-label="Portrait photo of the therapist" style="background:linear-gradient(#dde0e5,#f0f1f3)"></div>
    <svg class="badge" width="14" height="14" viewBox="0 0 14 14"><circle cx="7" cy="7" r="7" fill="#4dae45"/><path d="M4 7l2 2 4-4" fill="none" stroke="#fff" stroke-width="1.5"/></svg>
    <div class="r-name">Dr. Noam Levin</div>
    <div class="r-sub">General Therapist<br>MBBS / FCPS</div>
    <div class="r-div"></div>
    <div class="r-meta"><b>Area:</b>City 1<br><b>Category:</b>General, Emergency Mental Help<br><b>Sub-category:</b>Sub-category1</div>
    <div class="btn r-btn">Call Now</div>
    <div class="r-pay">Payment: Free<br>from: $300</div>
  </article>
  <article class="abs result" style="top:845px">
    <div class="avatar" role="img" aria-label="Portrait photo of the therapist" style="background:linear-gradient(#6a5fa8,#8a80c0)"></div>
    <svg class="badge" width="14" height="14" viewBox="0 0 14 14"><circle cx="7" cy="7" r="7" fill="#4dae45"/><path d="M4 7l2 2 4-4" fill="none" stroke="#fff" stroke-width="1.5"/></svg>
    <div class="r-name">Dr. Noam Levin</div>
    <div class="r-sub">General Therapist<br>MBBS / FCPS</div>
    <div class="r-div"></div>
    <div class="r-meta"><b>Area:</b>City 1<br><b>Category:</b>General, Emergency Mental Help<br><b>Sub-category:</b>Sub-category1</div>
    <div class="btn r-btn">Call Now</div>
    <div class="r-pay">Payment: Free<br>from: $300</div>
  </article>
  <article class="abs result" style="top:964px">
    <div class="avatar" role="img" aria-label="Portrait photo of the therapist" style="background:linear-gradient(#c42a55,#e0517a)"></div>
    <svg class="badge" width="14" height="14" viewBox="0 0 14 14"><circle cx="7" cy="7" r="7" fill="#4dae45"/><path d="M4 7l2 2 4-4" fill="none" stroke="#fff" stroke-width="1.5"/></svg>
    <div class="r-name">Dr. Noam Levin</div>
    <div class="r-sub">General Therapist<br>MBBS / FCPS</div>
    <div class="r-div"></div>
    <div class="r-meta"><b>Area:</b>City 1<br><b>Category:</b>General, Emergency Mental Help<br><b>Sub-category:</b>Sub-category1</div>
    <div class="btn r-btn">Call Now</div>
    <div class="r-pay">Payment: Free<br>from: $300</div>
  </article>
  <article class="abs result" style="top:1083px">
    <div class="avatar" role="img" aria-label="Portrait photo of the therapist" style="background:linear-gradient(#52b8b0,#7fd0c8)"></div>
    <svg class="badge" width="14" height="14" viewBox="0 0 14 14"><circle cx="7" cy="7" r="7" fill="#4dae45"/><path d="M4 7l2 2 4-4" fill="none" stroke="#fff" stroke-width="1.5"/></svg>
    <div class="r-name">Dr. Noam Levin</div>
    <div class="r-sub">General Therapist<br>MBBS / FCPS</div>
    <div class="r-div"></div>
    <div class="r-meta"><b>Area:</b>City 1<br><b>Category:</b>General, Emergency Mental Help<br><b>Sub-category:</b>Sub-category1</div>
    <div class="btn r-btn">Call Now</div>
    <div class="r-pay">Payment: Free<br>from: $300</div>
  </article>

  <p class="abs suggest">Do you have any suggestions? <a>Contact Us</a></p>
  <div class="abs rule-2"></div>

  <svg class="f-icon" style="left:126px" width="36" height="40" viewBox="0 0 36 40"><path d="M18 2L4 8v11c0 9 6 16 14 19 8-3 14-10 14-19V8z" fill="#e6eef8" stroke="#1e76c2" stroke-width="3"/><path d="M18 12v14M11 19h14" stroke="#1e76c2" stroke-width="4"/></svg>
  <div class="feature" style="left:184px"><h3>Therapists</h3><p>Lorem ipsum dolor sit amet, consectetur adipiscing elit, sed do eiusmod tempor incididunt ut labore et dolore magna aliqua.</p><div class="more">Find Therapists <svg width="12" height="8" viewBox="0 0 12 8"><path d="M0 4h10M7 1l3 3-3 3" fill="none" stroke="#4dae45" stroke-width="1.4"/></svg></div></div>
  <div class="col-rule" style="left:390px"></div>

  <svg class="f-icon" style="left:413px" width="46" height="42" viewBox="0 0 46 42"><path d="M23 22L2 31l21 10 21-10z" fill="#1e76c2"/><path d="M23 13L2 22l21 10 21-10z" fill="#5b9ad6"/><path d="M23 2L2 12l21 10 21-10z" fill="#a9c8ea"/></svg>
  <div class="feature" style="left:473px"><h3>Organizations</h3><p>Lorem ipsum dolor sit amet, consectetur adipiscing elit, sed do eiusmod tempor incididunt ut labore et dolore magna aliqua.</p><div class="more">Find Organizations <svg width="12" height="8" viewBox="0 0 12 8"><path d="M0 4h10M7 1l3 3-3 3" fill="none" stroke="#4dae45" stroke-width="1.4"/></svg></div></div>
  <div class="col-rule" style="left:678px"></div>

  <svg class="f-icon" style="left:701px" width="40" height="36" viewBox="0 0 40 36"><rect x="1" y="1" width="38" height="26" rx="4" fill="#8fb8e3"/><path d="M20 16l-10 19h20z" fill="#1e76c2"/></svg>
  <div class="feature" style="left:761px"><h3>Videos</h3><p>Lorem ipsum dolor sit amet, consectetur adipiscing elit, sed do eiusmod tempor incididunt ut labore et dolore magna aliqua.</p><div class="more">Video Library <svg width="12" height="8" viewBox="0 0 12 8"><path d="M0 4h10M7 1l3 3-3 3" fill="none" stroke="#4dae45" stroke-width="1.4"/></svg></div></div>

  <div class="abs foot-rule"></div>
  <div class="abs foot" style="left:111px">TovaLamarpe - Organization for Mental Health ©2023</div>
  <div class="abs foot foot-links" style="left:866px"><span>Privacy Policy</span><span>Terms</span></div>
</main>

<div class="abs sec-title" style="top:2080px">PRIMARY COLOR</div>
<div class="abs sec-copy" style="top:2110px">Brand or Main Product color for the entire design system.</div>
<div class="swatch" style="left:433px;top:2081px;background:var(--main)"></div>
<div class="swatch" style="left:601px;top:2081px;background:var(--green)"></div>
<div class="swatch" style="left:772px;top:2081px;background:var(--extra)"></div>
<div class="sw-name" style="left:442px;top:2161px">Main</div>
<div class="sw-hex" style="left:442px;top:2186px">#129E8</div>
<div class="sw-name" style="left:611px;top:2161px">Secondary</div>
<div class="sw-hex" style="left:611px;top:2186px">#19BD9</div>
<div class="sw-name" style="left:781px;top:2161px">Extra</div>
<div class="sw-hex" style="left:781px;top:2186px">#DCE6E5</div>

<div class="abs sec-title" style="top:2273px">SYSTEM COLORS</div>
<div class="abs sec-copy" style="top:2303px">Color collections for the entire product ecosystem</div>
<div class="swatch" style="left:433px;top:2274px;background:var(--dark)"></div>
<div class="swatch" style="left:601px;top:2274px;background:var(--grey)"></div>
<div class="swatch" style="left:772px;top:2274px;background:var(--light-grey)"></div>
<div class="swatch" style="left:942px;top:2274px;background:var(--light-grey-2)"></div>
<div class="sw-name" style="left:442px;top:2354px">Dark</div>
<div class="sw-name" style="left:611px;top:2354px">Grey</div>
<div class="sw-name" style="left:781px;top:2354px">Light Grey</div>
<div class="sw-name" style="left:952px;top:2354px">Light Grey 2</div>

</body>
</html>
```